HearthBond USA needs a Prayer booklet

I need a bookmark 2.5 x 8.5, full color, 2-sided, that lists a number of questions for married couples to ask themselves. The numbering is a little mixed up. Please make it look good.
My layout started with a different idea, but now would like it to be the shape of a larger bookmark.

Target Market(s)

Church

```html
<!DOCTYPE html>
<html lang="en">
<head>
<meta charset="utf-8">
<title>An Examination of Conscience for the Married – Bookmark</title>
<link href="https://fonts.googleapis.com/css2?family=Montserrat:wght@700&family=Nunito+Sans:ital,wght@0,400;0,600;0,700;1,700&display=swap" rel="stylesheet">
<style>
  :root {
    --navy: #0b4a6e;
    --teal: #5b9ab1;
    --ink: #1f4f73;
    --paper: #ffffff;
    --backdrop: #d3d4d6;
    --divider: #c9cacc;
  }
  * { margin: 0; padding: 0; box-sizing: border-box; }
  html, body { width: 1109px; height: 1200px; overflow: hidden; }
  body {
    background: var(--backdrop);
    position: relative;
    font-family: "Nunito Sans", Arial, sans-serif;
    color: var(--ink);
  }
  .bookmark {
    position: absolute;
    top: 177px;
    width: 254px;
    height: 864px;
    background: var(--paper);
    overflow: hidden;
  }
  .bookmark--front { left: 275px; }
  .bookmark--back { left: 586px; }

  .masthead {
    height: 147px;
    background: var(--navy);
    display: flex;
    align-items: flex-end;
    justify-content: center;
    padding-bottom: 8px;
  }
  .masthead h1 {
    font-family: "Montserrat", sans-serif;
    font-weight: 700;
    font-size: 19.5px;
    line-height: 22.6px;
    letter-spacing: 0.3px;
    color: var(--teal);
    text-align: center;
    width: 190px;
  }

  .questions {
    list-style: none;
    text-align: center;
    font-size: 8.6px;
    line-height: 12.8px;
  }
  .questions li { margin-bottom: 12.8px; }
  .bookmark--front .questions { padding: 6px 12px 0; }
  .bookmark--back .questions { padding: 53px 14px 0; height: 278px; }
  .blank-line {
    display: inline-block;
    width: 148px;
    border-bottom: 0.8px solid var(--ink);
    vertical-align: -1px;
  }

  .contrition {
    background: var(--navy);
    height: 170px;
    padding: 40px 14px 0;
    color: #fff;
    text-align: center;
  }
  .contrition h2 {
    font-family: "Nunito Sans", sans-serif;
    font-weight: 700;
    font-size: 19px;
    color: var(--teal);
    margin-bottom: 9px;
  }
  .contrition p {
    font-size: 8.5px;
    line-height: 12.8px;
    text-align: justify;
    text-align-last: center;
  }

  .divider { height: 3px; background: var(--divider); }

  .ministry {
    background: var(--navy);
    height: 124px;
    position: relative;
  }
  .ministry__tagline {
    position: absolute;
    right: 14px;
    top: 22px;
    font-style: italic;
    font-weight: 700;
    font-size: 9px;
    color: var(--teal);
  }
  .ministry__name {
    position: absolute;
    left: 16px;
    top: 56px;
    display: flex;
    align-items: center;
    gap: 10px;
    font-weight: 700;
    font-size: 19px;
    color: #fff;
    letter-spacing: 0.3px;
  }
  .ministry__mark {
    width: 20px;
    height: 20px;
    background: #fff;
  }

  .ordering {
    background: var(--navy);
    height: 266px;
    padding: 18px 14px 0;
    color: #fff;
    font-size: 8.6px;
    line-height: 12.8px;
    text-align: center;
  }
  .ordering .highlight { color: var(--teal); }
  .ordering .bold { font-weight: 700; color: var(--teal); letter-spacing: 0.2px; }

  .footer-bars {
    position: absolute;
    left: 0;
    bottom: 0;
    width: 100%;
    height: 15px;
    display: flex;
    gap: 2px;
  }
  .footer-bars span { display: block; height: 100%; }
  .footer-bars .side { background: var(--teal); flex: 0 0 79px; }
  .footer-bars .side:last-child { flex: 1; }
  .footer-bars .center { flex: 0 0 90px; }
  .bookmark--front .footer-bars .center { background: var(--navy); }
  .bookmark--back .footer-bars .center { background: #fff; }
  .bookmark--back .footer-bars { background: var(--navy); }
</style>
</head>
<body>

<section class="bookmark bookmark--front">
  <header class="masthead">
    <h1>AN EXAMINATION OF CONSCIENCE FOR THE MARRIED</h1>
  </header>
  <ol class="questions">
    <li>1. Have I said thoughtless or hurtful words,<br>yelled indiscriminately, or in any other<br>way been unkind oruncharitable to my<br>spouse or family members?</li>
    <li>2. Have I been angry at my spouse?</li>
    <li>3. Have I allowed resentments and bitterness<br>toward my spouse to take root in my mind?</li>
    <li>4. Has pride or selfishness caused me to stumble<br>and fall short in my marriage?</li>
    <li>5. Do I have an attitude that I’m right and<br>my spouse is always wrong?</li>
    <li>6. Have I been hard-hearted or callous?</li>
    <li>7. Have I been unfair, causing pain,<br>resentment and hurt in my marriage?</li>
    <li>8. Are my priorities misplaced?</li>
    <li>9. Am I defensive or critical of my spouse,<br>of my children?</li>
    <li>10. Have I been rude or self-seeking?</li>
    <li>11. Do I keep a record of wrongs?</li>
    <li>12. Have I been unsupportive?</li>
    <li>13. Have I spoken sharply or sarcastically to my spouse?<br>Have I spoken in a demeaning or negative way?</li>
    <li>14. Have I failed to seek God’s plan for our marriage?</li>
    <li>15. Has infidelity, pornography, overspending occurred?</li>
    <li>16. Have I failed to follow the teachings of the Church<br>on Family Planning?</li>
    <li>17. Have I failed to turn to God in prayer?</li>
    <li>18. Have I been unwilling to work to make our<br>marriage healthy?</li>
    <li>19. Have I failed to protect my spouse?</li>
    <li>20. Have I been unwilling to make changes<br>in my behavior? In my attitude? If so,<br>what has been the consequences?</li>
  </ol>
  <div class="footer-bars"><span class="side"></span><span class="center"></span><span class="side"></span></div>
</section>

<section class="bookmark bookmark--back">
  <ol class="questions">
    <li>21. Have I threatened to leave?<br>Or avoided the problems I create?</li>
    <li>22. Have I told little lies, or big ones?<br>Been imprecise in my words?</li>
    <li>23. Am I impatient with the ones I love?</li>
    <li>24. Have I physically abused my spouse?</li>
    <li>25. Have I gossiped about my spouse?</li>
    <li>26. Have I failed to seek forgiveness?</li>
    <li>27. Have I been unforgiving?</li>
    <li>28. <span class="blank-line"></span></li>
  </ol>

  <div class="contrition">
    <h2>Act of Contrition</h2>
    <p>O my God, I am heartily sorry for having offended you. And I detest all my sins because of your just punishment. But most of all because they offend you, my God, who art all-good and deserving of all my love. I firmly resolve, with the help of your grace, to sin no more, and to avoid the near occasion of sin. Amen.</p>
  </div>

  <div class="divider"></div>

  <div class="ministry">
    <p class="ministry__tagline">"..Rebuild My Church!"</p>
    <p class="ministry__name"><span class="ministry__mark"></span>HearthBond USA</p>
  </div>

  <div class="divider"></div>

  <div class="ordering">
    <p>Additional quantity copies of <span class="highlight">AN EXAMINATION OF CONSCIENCE FOR THE MARRIED</span> are available from <span class="bold">www.hearthbondusa.org</span> or by contacting Ned &amp; Laurie Hollis at <span class="bold">(815) 555-0147.</span></p>
  </div>

  <div class="footer-bars"><span class="side"></span><span class="center"></span><span class="side"></span></div>
</section>

</body>
</html>
```